Podcast Cover Art for Fast Growing Show (Ill include a gracious tip!)

This artwork is for "The Steadfast Fellow Show." The podcast is for men, and it's all about self-improvement, confidence, success, money, women and masculinity. It's for the guy who wants to improve himself. I'd like for my picture to be included — in black and white — and I want the text to read: "The Steadfast Fellow Show" and somewhere in there it'll say: "with Dale Prowen." I'm open to color schemes. The podcast is a little edgy so I'd like for that to be represented in the design. Thank you! (((Here's the podcast page if you wanna check it out: http://steadfastfellowshow.castorbit.net/)))

Target Market(s)

Men who want to attract women and improve their lives!

Font styles to use
Serif

Colors

Designer to choose colors to be used in the design.

Requirements
Must have
• My image in it (in black and white) and the two titles: "The Steadfast Fellow Show" and "with Dale Prowen"
Nice to have
• My logo in it somehow (which is the arrow looking logo attached below). I've also found that my image looks best in black and white and with a circular type cut out (although I'm open to different design ideas). I've attached my logo with a circular cut out below so you can see what I'm talking about.
Should not have
• Flowers. Teddy bears. ice cream.

```html
<!DOCTYPE html>
<html lang="en">
<head>
<meta charset="utf-8">
<title>The Steadfast Fellow Show – Cover Art, 4 in One</title>
<link rel="stylesheet" href="https://fonts.googleapis.com/css2?family=Inter:ital,wght@0,300;0,700;1,700&family=Source+Serif+4:ital,wght@1,600&display=swap">
<style>
  :root {
    --ink: #000000;
    --paper: #ffffff;
    --stage: #e6e6e6;
    --stage-shade: #9a9a9a;
    --accent-red: #e0252b;
    --accent-blue: #2a2cff;
    --with-red: #d63c3c;
    --mono-light: #8c8c8c;
  }
  * { box-sizing: border-box; margin: 0; padding: 0; }
  html, body { width: 1200px; height: 4445px; overflow: hidden; }
  body {
    position: relative;
    background: linear-gradient(90deg, var(--stage) 0%, var(--stage-shade) 22%, var(--stage-shade) 78%, var(--stage) 100%);
    font-family: "Inter", Arial, sans-serif;
  }
  .cover {
    position: absolute;
    left: 97px;
    width: 1006px;
    height: 1006px;
    background: var(--ink);
    overflow: hidden;
    box-shadow: 0 0 70px rgba(0,0,0,0.55);
  }
  .cover--one   { top: 69px; }
  .cover--two   { top: 1134px; }
  .cover--three { top: 2200px; }
  .cover--four  { top: 3265px; }

  .portrait {
    position: absolute;
    left: 60px;
    top: 130px;
    width: 900px;
    height: 876px;
  }
  .portrait--duotone {
    background:
      radial-gradient(ellipse 26% 36% at 36% 38%, rgba(224,37,43,0.85), rgba(224,37,43,0) 100%),
      radial-gradient(ellipse 26% 36% at 64% 38%, rgba(42,44,255,0.85), rgba(42,44,255,0) 100%),
      radial-gradient(ellipse 60% 40% at 30% 95%, rgba(120,20,24,0.55), rgba(0,0,0,0) 100%),
      radial-gradient(ellipse 60% 40% at 70% 95%, rgba(20,22,120,0.55), rgba(0,0,0,0) 100%);
  }
  .portrait--mono {
    background:
      radial-gradient(ellipse 30% 40% at 50% 36%, rgba(170,170,170,0.9), rgba(0,0,0,0) 100%),
      radial-gradient(ellipse 70% 40% at 50% 95%, rgba(70,70,70,0.7), rgba(0,0,0,0) 100%);
  }

  .title {
    position: absolute;
    top: 78px;
    left: 41px;
    width: 925px;
    color: var(--paper);
    font-weight: 700;
    font-size: 92px;
    line-height: 1;
    letter-spacing: -3px;
    white-space: nowrap;
  }
  .cover--one .title { left: 24px; }
  .title__show {
    display: block;
    text-align: right;
    font-style: italic;
    font-size: 64px;
    letter-spacing: 0;
    margin-top: -4px;
    padding-right: 4px;
  }

  .host {
    position: absolute;
    left: 52px;
    top: 900px;
    color: var(--paper);
    font-family: "Source Serif 4", Georgia, serif;
    font-style: italic;
    font-weight: 600;
    font-size: 58px;
    line-height: 1;
  }
  .cover--one .host { left: 36px; }
  .host__with--red { color: var(--with-red); }

  .brand {
    position: absolute;
    right: 80px;
    top: 900px;
    color: var(--paper);
    font-weight: 700;
    font-size: 30px;
    letter-spacing: 2px;
    display: flex;
    align-items: center;
    gap: 12px;
  }
  .cover--one .brand { right: 110px; }
  .brand__mark { width: 22px; height: 22px; background: var(--paper); }

  .edge-bar {
    position: absolute;
    top: 0;
    right: 27px;
    width: 11px;
    height: 1006px;
    background: var(--paper);
  }
  .inset-frame {
    position: absolute;
    inset: 0;
    border: 20px solid var(--paper);
    pointer-events: none;
  }

  .footer-band {
    position: absolute;
    left: 0;
    top: 4354px;
    width: 1200px;
    height: 91px;
    background: var(--ink);
    color: var(--paper);
    font-weight: 300;
    font-size: 58px;
    letter-spacing: 2px;
    text-align: center;
    line-height: 91px;
  }
</style>
</head>
<body>

  <section class="cover cover--one">
    <div class="portrait portrait--duotone" role="img" aria-label="Host portrait, hands steepled, lit red from the left and blue from the right"></div>
    <h1 class="title">The Steadfast Fellow<span class="title__show">Show</span></h1>
    <p class="host"><span class="host__with">with</span> Dale Prowen</p>
    <div class="brand"><span class="brand__mark"></span>STEADFAST</div>
    <div class="edge-bar"></div>
  </section>

  <section class="cover cover--two">
    <div class="portrait portrait--duotone" role="img" aria-label="Host portrait, hands steepled, lit red from the left and blue from the right"></div>
    <h2 class="title">The Steadfast Fellow<span class="title__show">Show</span></h2>
    <p class="host"><span class="host__with host__with--red">with</span> Dale Prowen</p>
    <div class="brand"><span class="brand__mark"></span>STEADFAST</div>
  </section>

  <section class="cover cover--three">
    <div class="portrait portrait--duotone" role="img" aria-label="Host portrait, hands steepled, lit red from the left and blue from the right"></div>
    <h2 class="title">The Steadfast Fellow<span class="title__show">Show</span></h2>
    <p class="host"><span class="host__with host__with--red">with</span> Dale Prowen</p>
    <div class="brand"><span class="brand__mark"></span>STEADFAST</div>
    <div class="inset-frame"></div>
  </section>

  <section class="cover cover--four">
    <div class="portrait portrait--mono" role="img" aria-label="Host portrait in black and white, hands steepled"></div>
    <h2 class="title">The Steadfast Fellow<span class="title__show">Show</span></h2>
    <p class="host"><span class="host__with">with</span> Dale Prowen</p>
    <div class="brand"><span class="brand__mark"></span>STEADFAST</div>
  </section>

  <footer class="footer-band">4 IN ONE</footer>

</body>
</html>
```